Marlow Law Stationery - Letterhead, Envelopes, Business Cards

We need high quality business stationery for our Personal Injury Law Firm located in Houston, Texas. The design should include the logo, Marlow Law Group, PLLC, 713-555-4718, 2150 Fernbrook Avenue, Suite 310, Houston, Texas 77019 www.MarlowLaw.example. The colors are blue and white. The letterhead should also include the Attorneys - Tessa Quill, Mitchell R. Marlow and Derek Hale.

```html
<!DOCTYPE html>
<html lang="en">
<head>
<meta charset="utf-8">
<title>Marlow Law Business Cards</title>
<link href="https://fonts.googleapis.com/css2?family=Montserrat:wght@400;600;700;800&display=swap" rel="stylesheet">
<style>
  :root {
    --navy: #0f1f3d;
    --ink: #2b3445;
    --muted: #4a5262;
    --rule: #3a3f4a;
    --card: #ffffff;
    --backdrop: #e8e8e8;
  }
  * { box-sizing: border-box; margin: 0; padding: 0; }
  html, body { width: 1200px; height: 1200px; overflow: hidden; }
  body {
    background: var(--backdrop);
    font-family: "Montserrat", Arial, sans-serif;
    position: relative;
  }
  .card {
    position: absolute;
    width: 495px;
    height: 283px;
    background: var(--card);
  }
  .brand {
    position: absolute;
    top: 45px;
    right: 45px;
    display: flex;
    align-items: center;
    gap: 6px;
  }
  .brand-dot {
    width: 56px;
    height: 56px;
    border-radius: 50%;
    background: var(--navy);
  }
  .brand-text {
    color: var(--navy);
    font-weight: 700;
    text-align: right;
    line-height: 1;
  }
  .brand-name { font-size: 9.6px; letter-spacing: 0.1px; display: block; margin-bottom: 3px; }
  .brand-tag { font-size: 23px; display: block; line-height: 1.02; }
  .person {
    position: absolute;
    left: 45px;
    right: 45px;
    top: 143px;
  }
  .person-name {
    color: var(--navy);
    font-weight: 700;
    font-size: 17px;
    letter-spacing: -0.2px;
    line-height: 1;
  }
  .title-row {
    display: flex;
    align-items: center;
    gap: 4px;
    margin-top: 2px;
  }
  .person-title { color: var(--muted); font-size: 13px; white-space: nowrap; }
  .title-rule { flex: 1; height: 1px; background: var(--rule); }
  .contact {
    position: absolute;
    left: 45px;
    right: 45px;
    top: 188px;
    display: flex;
    justify-content: space-between;
    color: var(--muted);
    font-size: 12.8px;
    line-height: 16.3px;
  }
  .contact-list { list-style: none; }
  .contact-list li { display: flex; align-items: center; gap: 5px; }
  .contact-list svg { width: 11px; height: 11px; fill: var(--navy); flex: none; }
  .address { font-style: normal; text-align: right; }
</style>
</head>
<body>
<svg width="0" height="0" style="position:absolute">
  <defs>
    <symbol id="icon-phone" viewBox="0 0 12 12"><path d="M1 4c0-2 2-3 5-3s5 1 5 3l-2 1-1-1.5H4L3 5zM3 5.5h6l1.5 5h-9z"/><circle cx="6" cy="8" r="1.4" fill="#fff"/></symbol>
    <symbol id="icon-mail" viewBox="0 0 12 12"><path d="M0.5 2.5h11v7h-11z"/><path d="M0.8 2.8L6 7l5.2-4.2" stroke="#fff" stroke-width="1" fill="none"/></symbol>
    <symbol id="icon-web" viewBox="0 0 12 12"><circle cx="6" cy="6" r="5.5"/><path d="M4 2.5c1 1 0 2 1 3s2 0 2 1.5-1 1.5-1 3M8 2c-.5 1 .5 1.5 1.5 1.5" stroke="#fff" stroke-width="1" fill="none"/></symbol>
  </defs>
</svg>

<article class="card" style="left:90px;top:152px">
  <div class="brand"><span class="brand-dot"></span><div class="brand-text"><span class="brand-name">MARLOW LAW GROUP, PLLC</span><span class="brand-tag">INJURY<br>ATTORNEYS</span></div></div>
  <div class="person"><h2 class="person-name">TESSA QUILL</h2><div class="title-row"><span class="person-title">Managing Partner</span><span class="title-rule"></span></div></div>
  <div class="contact">
    <ul class="contact-list"><li><svg><use href="#icon-phone"/></svg>713-555-4718</li><li><svg><use href="#icon-mail"/></svg>Tessa@MarlowLaw.example</li><li><svg><use href="#icon-web"/></svg>www.marlowlaw.example</li></ul>
    <address class="address">2150 Fernbrook Avenue<br>Suite 310<br>Houston, TX 77019</address>
  </div>
</article>

<article class="card" style="left:612px;top:150px">
  <div class="brand"><span class="brand-dot"></span><div class="brand-text"><span class="brand-name">MARLOW LAW GROUP, PLLC</span><span class="brand-tag">INJURY<br>ATTORNEYS</span></div></div>
  <div class="person"><h2 class="person-name">MITCHELL R. MARLOW</h2><div class="title-row"><span class="person-title">Senior Partner</span><span class="title-rule"></span></div></div>
  <div class="contact">
    <ul class="contact-list"><li><svg><use href="#icon-phone"/></svg>713-555-4718</li><li><svg><use href="#icon-mail"/></svg>Mitch@MarlowLaw.example</li><li><svg><use href="#icon-web"/></svg>www.marlowlaw.example</li></ul>
    <address class="address">2150 Fernbrook Avenue<br>Suite 310<br>Houston, TX 77019</address>
  </div>
</article>

<article class="card" style="left:91px;top:459px">
  <div class="brand"><span class="brand-dot"></span><div class="brand-text"><span class="brand-name">MARLOW LAW GROUP, PLLC</span><span class="brand-tag">INJURY<br>ATTORNEYS</span></div></div>
  <div class="person"><h2 class="person-name">NADIA PRUITT</h2><div class="title-row"><span class="person-title">Legal Assistant</span><span class="title-rule"></span></div></div>
  <div class="contact">
    <ul class="contact-list"><li><svg><use href="#icon-phone"/></svg>713-555-4718</li><li><svg><use href="#icon-mail"/></svg>Nadia@MarlowLaw.example</li><li><svg><use href="#icon-web"/></svg>www.marlowlaw.example</li></ul>
    <address class="address">2150 Fernbrook Avenue<br>Suite 310<br>Houston, TX 77019</address>
  </div>
</article>

<article class="card" style="left:613px;top:457px">
  <div class="brand"><span class="brand-dot"></span><div class="brand-text"><span class="brand-name">MARLOW LAW GROUP, PLLC</span><span class="brand-tag">INJURY<br>ATTORNEYS</span></div></div>
  <div class="person"><h2 class="person-name">LENA VOSS</h2><div class="title-row"><span class="person-title">Office Manager</span><span class="title-rule"></span></div></div>
  <div class="contact">
    <ul class="contact-list"><li><svg><use href="#icon-phone"/></svg>713-555-4718</li><li><svg><use href="#icon-mail"/></svg>Lena@MarlowLaw.example</li><li><svg><use href="#icon-web"/></svg>www.marlowlaw.example</li></ul>
    <address class="address">2150 Fernbrook Avenue<br>Suite 310<br>Houston, TX 77019</address>
  </div>
</article>

<article class="card" style="left:92px;top:767px">
  <div class="brand"><span class="brand-dot"></span><div class="brand-text"><span class="brand-name">MARLOW LAW GROUP, PLLC</span><span class="brand-tag">INJURY<br>ATTORNEYS</span></div></div>
  <div class="person"><h2 class="person-name">OWEN TARRANT</h2><div class="title-row"><span class="person-title">Legal Assistant</span><span class="title-rule"></span></div></div>
  <div class="contact">
    <ul class="contact-list"><li><svg><use href="#icon-phone"/></svg>713-555-4718</li><li><svg><use href="#icon-mail"/></svg>Owen@MarlowLaw.example</li><li><svg><use href="#icon-web"/></svg>www.marlowlaw.example</li></ul>
    <address class="address">2150 Fernbrook Avenue<br>Suite 310<br>Houston, TX 77019</address>
  </div>
</article>

<article class="card" style="left:614px;top:765px">
  <div class="brand"><span class="brand-dot"></span><div class="brand-text"><span class="brand-name">MARLOW LAW GROUP, PLLC</span><span class="brand-tag">INJURY<br>ATTORNEYS</span></div></div>
  <div class="person"><h2 class="person-name">CORINNE ABBOT</h2><div class="title-row"><span class="person-title">Paralegal</span><span class="title-rule"></span></div></div>
  <div class="contact">
    <ul class="contact-list"><li><svg><use href="#icon-phone"/></svg>713-555-4718</li><li><svg><use href="#icon-mail"/></svg>Corinne@MarlowLaw.example</li><li><svg><use href="#icon-web"/></svg>www.marlowlaw.example</li></ul>
    <address class="address">2150 Fernbrook Avenue<br>Suite 310<br>Houston, TX 77019</address>
  </div>
</article>
</body>
</html>
```